Simple HVAC & Electrical Contractor Billboard

Leasing a 12'3" H by 49'3" W billboard. I'd like to use our current logo and add a few words to let people know what we do. Looking for a clean simple look.
Our company name is Harold Pruett Mechanical - What we are is Air Conditioning & Electrical Contractors.

Our license numbers are TACLA00052916K & TECL71420 they will need to be visible on the sign somewhere.

I'm not sure how much information I want to see on the sign. I want to keep it clean but some of our contact info is as follows. Office # 555-208-4619 - Webpage hpmexample.com. I feel like most people can search the name to find the contact info they need but I'll defer to the designers to come up with the best design.

I have attached a couple different logos we have used I the past.

```html
<!DOCTYPE html>
<html lang="en">
<head>
<meta charset="utf-8">
<title>Harold Pruett Mechanical – Billboard</title>
<link rel="stylesheet" href="https://fonts.googleapis.com/css2?family=Montserrat:wght@700&family=Oswald:wght@300;400&display=swap">
<style>
  :root {
    --board-black: #1e1e1e;
    --brand-red: #ec1f26;
    --ink-white: #ffffff;
    --ink-dark: #1e1e1e;
    --page-bg: #ffffff;
  }
  html, body {
    margin: 0;
    padding: 0;
    width: 1200px;
    height: 1025px;
    overflow: hidden;
    background: var(--page-bg);
  }
  .billboard {
    position: absolute;
    left: 40px;
    top: 373px;
    width: 1120px;
    height: 279px;
    box-shadow: 0 2px 6px rgba(0,0,0,0.25);
  }
  .board-bg { fill: var(--board-black); }
  .accent-red { fill: var(--brand-red); }
  .accent-white { fill: var(--ink-white); }
  .divider { stroke: var(--ink-white); stroke-width: 2; }
  .contact-phone {
    font-family: "Oswald", sans-serif;
    font-weight: 300;
    font-size: 66px;
    fill: var(--ink-white);
  }
  .contact-web {
    font-family: "Oswald", sans-serif;
    font-weight: 300;
    font-size: 36px;
    fill: var(--ink-white);
  }
  .brand-name {
    font-family: "Montserrat", sans-serif;
    font-weight: 700;
    fill: var(--ink-white);
  }
  .brand-name-main { font-size: 36px; }
  .brand-name-sub { font-size: 18px; }
  .service-line {
    font-family: "Oswald", sans-serif;
    font-weight: 400;
    font-size: 29px;
  }
  .service-line.white { fill: var(--ink-white); }
  .service-line.red { fill: var(--brand-red); }
  .service-small { font-size: 21px; }
  .license-text {
    font-family: "Montserrat", sans-serif;
    font-weight: 700;
    font-size: 21px;
    fill: var(--ink-dark);
  }
</style>
</head>
<body>
  <svg class="billboard" viewBox="0 0 1120 279" width="1120" height="279" xmlns="http://www.w3.org/2000/svg" role="img" aria-label="Harold Pruett Mechanical billboard">
    <rect class="board-bg" x="0" y="0" width="1120" height="279"/>

    <!-- corner accents -->
    <polygon class="accent-red" points="0,0 74,0 0,58"/>
    <polygon class="accent-white" points="110,0 124,0 0,96 0,84"/>
    <polygon class="accent-red" points="1047,0 1120,0 1120,58"/>
    <polygon class="accent-white" points="996,0 1010,0 1120,88 1120,100"/>

    <!-- contact column -->
    <g class="contact">
      <text class="contact-phone" x="41" y="130" textLength="248" lengthAdjust="spacingAndGlyphs">555-208-4619</text>
      <text class="contact-web" x="41" y="168" textLength="247" lengthAdjust="spacingAndGlyphs">WWW.HPMEXAMPLE.COM</text>
    </g>

    <line class="divider" x1="347" y1="46" x2="347" y2="208"/>

    <!-- brand column -->
    <g class="brand">
      <rect class="accent-red" x="538" y="36" width="72" height="72"/>
      <text class="brand-name brand-name-main" x="574" y="172" text-anchor="middle" textLength="340" lengthAdjust="spacingAndGlyphs">HAROLD PRUETT</text>
      <text class="brand-name brand-name-sub" x="574" y="202" text-anchor="middle" textLength="210" lengthAdjust="spacing">MECHANICAL</text>
    </g>

    <line class="divider" x1="800" y1="46" x2="800" y2="208"/>

    <!-- services column -->
    <g class="services">
      <text class="service-line white" x="827" y="94" textLength="195" lengthAdjust="spacingAndGlyphs">AIR CONDITIONING &amp;</text>
      <text class="service-line red" x="827" y="124" textLength="248" lengthAdjust="spacingAndGlyphs">ELECTRICAL CONTRACTORS</text>
      <text class="service-line white" x="827" y="150" textLength="190" lengthAdjust="spacingAndGlyphs">SPECIALIZING<tspan class="service-small"> IN SERVICE &amp;</tspan></text>
      <text class="service-line red" x="827" y="180" textLength="131" lengthAdjust="spacingAndGlyphs">INSTALLATION</text>
    </g>

    <!-- license band -->
    <rect class="accent-red" x="0" y="234" width="1120" height="33"/>
    <rect class="accent-white" x="221" y="234" width="678" height="33"/>
    <text class="license-text" x="560" y="258" text-anchor="middle" textLength="626" lengthAdjust="spacingAndGlyphs">LICENSE NUMBER: TACLA00052916K &amp; TECL71420</text>
  </svg>
</body>
</html>
```